Steelcrest Process Systems. Needs a Business Card Design

We need a business card design for an engineering company which supplies industrial components (pumps, compressors, mechanical seals) provides repairs and services for above mentioned equipments. We offer a uniqe engineering solutions which help our customers to increase the productivness of their manufacturings, and energy savings.

Target Market(s)

Chemical and energy plants, refineries. Food industry and private consumers in a less.

Industry/Entity Type

Business

Contact Information for Business Card

Stylish and sleek design oriented on industrial area.

Requirements
Should not have
• company name shortening

```html
<!DOCTYPE html>
<html lang="en">
<head>
<meta charset="utf-8">
<title>Steelcrest Process Systems – Business Card</title>
<link rel="stylesheet" href="https://fonts.googleapis.com/css2?family=Ubuntu:wght@400;500;700&display=swap">
<style>
  :root {
    --brand-blue: #1b3f9b;
    --paper: #ffffff;
    --stage: #e9e7e3;
    --faint-grey: #e6e6e6;
    --text-white: #ffffff;
  }
  * { margin: 0; padding: 0; box-sizing: border-box; }
  html, body {
    width: 1200px; height: 900px; overflow: hidden;
    background: var(--stage);
    font-family: "Ubuntu", sans-serif;
  }
  .stage { position: relative; width: 1200px; height: 900px; }

  .card {
    position: absolute; width: 630px; height: 360px; overflow: hidden;
    box-shadow: 0 10px 28px rgba(0,0,0,0.18);
  }

  /* Back side: contact details */
  .card-back { left: 70px; top: 70px; background: var(--brand-blue); color: var(--text-white); }
  .card-back .brand {
    position: absolute; left: 40px; top: 90px; width: 190px;
    display: flex; flex-direction: column; align-items: flex-start; gap: 14px;
  }
  .card-back .brand-dot { width: 26px; height: 26px; border-radius: 50%; background: var(--text-white); }
  .card-back .brand-name { font-size: 26px; font-weight: 700; line-height: 1.15; }
  .card-back .divider {
    position: absolute; left: 240px; top: 92px; width: 1px; height: 150px;
    background: rgba(255,255,255,0.55);
  }
  .contact { position: absolute; left: 264px; top: 84px; width: 270px; }
  .contact .person-name { font-size: 20px; font-weight: 700; letter-spacing: 0.3px; }
  .contact .person-title { font-size: 16px; margin-top: 4px; }
  .contact .lines { margin-top: 22px; font-size: 15px; line-height: 1.6; }
  .contact .line { display: flex; align-items: center; gap: 8px; white-space: nowrap; }
  .contact .icon { width: 14px; height: 14px; flex: none; }

  .service-band {
    position: absolute; left: 0; right: 0; bottom: 22px; height: 40px;
    background: var(--paper); color: var(--brand-blue);
    display: flex; align-items: center; padding-left: 40px;
    font-size: 18px; font-weight: 500;
  }
  .corner-tab {
    position: absolute; right: 28px; top: 0; width: 50px; height: 298px;
    background: var(--paper);
  }
  .corner-mark {
    position: absolute; right: 37px; top: 22px; width: 32px; height: 32px;
    border-radius: 50%; background: var(--brand-blue);
  }

  /* Front side: company name */
  .card-front { left: 500px; top: 470px; background: var(--paper); }
  .card-front .faint-circle {
    position: absolute; right: -80px; bottom: -200px; width: 300px; height: 300px;
    border-radius: 50%; background: var(--faint-grey);
  }
  .card-front .brand {
    position: absolute; left: 0; right: 0; top: 105px;
    display: flex; flex-direction: column; align-items: center; gap: 22px;
  }
  .card-front .brand-dot { width: 60px; height: 60px; border-radius: 50%; background: var(--brand-blue); }
  .card-front .brand-name { font-size: 34px; font-weight: 700; color: var(--brand-blue); }
</style>
</head>
<body>
<main class="stage">

  <section class="card card-back" aria-label="Business card back">
    <div class="corner-tab"></div>
    <div class="corner-mark"></div>

    <div class="brand">
      <span class="brand-dot"></span>
      <span class="brand-name">Steelcrest Process Systems</span>
    </div>

    <div class="divider"></div>

    <div class="contact">
      <p class="person-name">YOUR NAME HERE</p>
      <p class="person-title">Title here</p>
      <div class="lines">
        <p class="line">Your Address here, Your Address here</p>
        <p class="line">
          <svg class="icon" viewBox="0 0 14 14"><rect width="14" height="14" rx="2" fill="#fff"/><path d="M4 3.5h2l.8 2-1.2.8a5 5 0 0 0 2.1 2.1l.8-1.2 2 .8v2a1 1 0 0 1-1 1A6.5 6.5 0 0 1 3 4.5a1 1 0 0 1 1-1z" fill="#1b3f9b"/></svg>
          0471-5520-8190
        </p>
        <p class="line">
          <svg class="icon" viewBox="0 0 14 14"><rect width="14" height="14" rx="2" fill="#fff"/><rect x="3" y="4" width="8" height="6" fill="none" stroke="#1b3f9b" stroke-width="1.2"/><path d="M3 4l4 3.2L11 4" fill="none" stroke="#1b3f9b" stroke-width="1.2"/></svg>
          office@steelcrest.com
        </p>
      </div>
    </div>

    <div class="service-band">Pumps, Compressors, Mechanical Seals and Services</div>
  </section>

  <section class="card card-front" aria-label="Business card front">
    <div class="faint-circle"></div>
    <div class="brand">
      <span class="brand-dot"></span>
      <span class="brand-name">Steelcrest Process Systems</span>
    </div>
  </section>

</main>
</body>
</html>
```